Unternehmensbroschüre für Personaldienstleister
Die Zusammenarbeit mit Annika war sehr produktiv und angenehm. Sie ist sehr professionell, kreativ und konnte unsere Vorstellungen super umsetzen. Auf jeden Fall weiter zu empfehlen!
Zielgruppe
Weidmann & Kollegen ist führend in der schnellen Bereitstellung von Spezialisten und Teams für anspruchsvolle ICT und Business Projekte. Beginnend beim Bereitstellen eines einzelnen erfolgskritischen Fachspezialisten, bis hin zum Einsatz einer gesamten Projekt-Taskforce, sichern wir den Erfolg unserer Kunden in der digitalen Zukunft.
Seit über 25 Jahren sind wir erfolgreich im Personalverleih von IT-Spezialisten tätig und haben uns ein grosses Know-how in den Branchen Banken, Versicherungen und öffentliche Hand aufgebaut.
Aufgabenstellung
Wir sind Personaldienstleister und benötigen eine Unternehmensbroschüre in unserem Corporate Design (PDF und InDesign). Das Corporate Design ist auf die Broschüre anzuwenden. Im Anhang finden Sie Dateien zum Corporate Design (Schrift, Logo, Claim, Farbwerte und Manual).
Die Broschüre soll im A4 Format erstellt werden und 12 Seiten beinhalten.
Es gibt einen ersten Entwurf vom Texter sowie ein grobe Richtung, wie die Seiten verteilt werden soll. Dieser ist im Anhang beigefügt. kann jedoch noch angepasst werden. Auch die Verteilung der Seiten soll eine grobe Richtung vorgeben und kann individuell angepasst werden. Uns ist wichtig, dass die Bilder/ Graphiken Emotionen wecken und die textlichen Bausteine diese unterstützen. Der Text sollte nicht zu lang sein und ein gutes Verhältnis zu den Bildern darstellen.
Bei den Fotos können Sie Vorschläge aus Fotodatenbanken machen (optimalerweise aus Lumora Bildpool).
Ein Beispiel welches uns gut gefällt ist die Broschüre von dem Unternehmen Tempokraftwerk (siehe Anhang). Es bietet ein gutes Verhältnis zwischen Bilder, Icons und Text. Auf den Seiten 8-11 werden mit der Bildersprache (Berg, Holz ) die Aussagen entsprechend unterstützt.

```html
<!DOCTYPE html>
<html lang="de">
<head>
<meta charset="utf-8">
<title>Weidmann &amp; Kollegen – Vorwort CEO</title>
<link href="https://fonts.googleapis.com/css2?family=Montserrat:wght@600;700;800&family=Mulish:wght@400;700;800&display=swap" rel="stylesheet">
<style>
  :root{
    --bg:#e4e4e4;
    --paper:#f7f7f7;
    --ink:#1d1d1f;
    --text:#3c3c3e;
    --blue:#5a8fd0;
    --sky:#7fbfe6;
    --green:#6cbf86;
    --num-blue:#c9dbe6;
    --num-teal:#c6dcd8;
    --num-green:#cfe3d3;
    --rule:#8a8a8a;
  }
  *{margin:0;padding:0;box-sizing:border-box}
  html,body{width:1200px;height:848px;overflow:hidden;background:var(--bg)}
  body{font-family:"Mulish",sans-serif;color:var(--text)}
  .spread{position:absolute;left:48px;top:34px;width:1104px;height:780px;display:flex;box-shadow:0 10px 30px rgba(0,0,0,.12)}
  .page{position:relative;width:552px;height:780px;overflow:hidden}

  /* left page */
  .page--quote{color:#fff}
  .page--quote svg.backdrop{position:absolute;inset:0}
  .quote-mark{position:absolute;left:96px;top:250px;font-family:"Montserrat",sans-serif;font-weight:800;font-size:96px;line-height:1;letter-spacing:-6px}
  .quote-text{position:absolute;left:96px;top:318px;font-family:"Montserrat",sans-serif;font-weight:700;font-size:33px;line-height:1.08;letter-spacing:1.5px;text-transform:uppercase}
  .claim{position:absolute;left:28px;bottom:110px;writing-mode:vertical-rl;transform:rotate(180deg);font-size:7px;letter-spacing:1.4px;font-weight:700;text-transform:uppercase;opacity:.85}
  .folio-left{position:absolute;left:28px;bottom:78px;font-size:8px;width:70px;border-top:1px solid rgba(255,255,255,.6);padding-top:4px}

  /* right page */
  .page--intro{background:var(--paper)}
  .section-label{position:absolute;right:40px;top:150px;font-size:8px;font-weight:700;letter-spacing:.8px;color:var(--ink)}
  .portrait{position:absolute;left:0;top:196px;width:214px;height:144px;background:linear-gradient(135deg,#8b8f8a 0%,#5d615e 45%,#2a2c2e 100%)}
  .portrait-caption{position:absolute;left:120px;top:300px;color:#fff;font-weight:700;font-size:10px;line-height:1.2}
  .portrait-caption span{display:block;font-weight:400;font-size:8px}
  .headline{position:absolute;left:232px;top:196px;width:290px;font-family:"Montserrat",sans-serif;font-weight:700;font-size:17px;line-height:1.1;color:var(--blue);text-transform:uppercase;letter-spacing:.6px}
  .lead{position:absolute;left:232px;top:244px;width:290px;font-size:10.6px;line-height:1.42;color:var(--ink)}
  .lead strong{font-weight:800}
  .facts{position:absolute;left:40px;top:392px;width:470px}
  .fact{display:flex;gap:18px;margin-bottom:12px}
  .fact-num{width:78px;flex:none;font-family:"Montserrat",sans-serif;font-weight:700;font-size:44px;line-height:1;letter-spacing:2px}
  .fact:nth-child(1) .fact-num{color:var(--num-blue)}
  .fact:nth-child(2) .fact-num{color:var(--num-teal)}
  .fact:nth-child(3) .fact-num{color:var(--num-green)}
  .fact h3{font-size:8px;font-weight:800;color:var(--sky);text-transform:uppercase;letter-spacing:.4px;margin-bottom:2px}
  .fact p{font-size:8px;line-height:1.42}
  .closing{position:absolute;left:40px;top:636px;width:330px;border-top:1px solid var(--rule);padding-top:10px;font-size:10px;line-height:1.4;color:var(--ink)}
  .closing strong{font-weight:800;display:block;margin-top:6px}
  .signature{display:block;width:140px;height:26px;margin-top:6px;background:linear-gradient(90deg,#d9d9d9,#ececec)}
  .rule-vertical{position:absolute;left:468px;top:650px;width:1px;height:98px;background:var(--rule)}
  .folio-right{position:absolute;left:442px;top:748px;width:76px;border-top:1px solid var(--rule);padding-top:4px;font-size:8px}
</style>
</head>
<body>
<main class="spread">
  <section class="page page--quote">
    <svg class="backdrop" width="552" height="780" viewBox="0 0 552 780" aria-hidden="true">
      <defs>
        <linearGradient id="pageGrad" x1="0" y1="0" x2="0.6" y2="1">
          <stop offset="0" stop-color="#5484c0"/>
          <stop offset="0.45" stop-color="#6aa6d8"/>
          <stop offset="0.7" stop-color="#6fb7cf"/>
          <stop offset="1" stop-color="#69bd82"/>
        </linearGradient>
        <linearGradient id="glow" x1="0" y1="0" x2="1" y2="0">
          <stop offset="0" stop-color="#8fc8ea" stop-opacity="0"/>
          <stop offset="1" stop-color="#8fc8ea" stop-opacity=".75"/>
        </linearGradient>
      </defs>
      <rect width="552" height="780" fill="url(#pageGrad)"/>
      <rect x="300" width="252" height="780" fill="url(#glow)"/>
      <circle cx="130" cy="640" r="300" fill="#ffffff" opacity=".08"/>
      <circle cx="20" cy="720" r="180" fill="#2f7a6a" opacity=".12"/>
    </svg>
    <div class="quote-mark">”</div>
    <p class="quote-text">Die Suche<br>nach ICT-<br>Spezialisten?<br>Eine Vertrauens-<br>sache.</p>
    <div class="claim">Digital. Business. People.</div>
    <div class="folio-left">02</div>
  </section>

  <section class="page page--intro">
    <div class="section-label">– VORWORT CEO</div>
    <div class="portrait" role="img" aria-label="Porträtfoto von Reto Albrecht, CEO"></div>
    <div class="portrait-caption">Reto Albrecht<span>CEO</span></div>
    <h2 class="headline">ICT-Jobs bleiben immer länger unbesetzt.</h2>
    <p class="lead"><strong>Manche Unternehmen benötigen 4 bis 6 Monate, um eine Stelle zu besetzen.</strong> Wer kann sich das Warten schon leisten, bis der passende IT-Experte gefunden und eingearbeitet worden ist? Schliesslich müssen Unternehmen immer schneller auf wechselnde Business-Anforderungen reagieren. Wer seine Produkte und Services nicht rechtzeitig zur Marktreife entwickelt, verliert Wettbewerbsvorteile und Marktanteile.</p>

    <div class="facts">
      <div class="fact">
        <div class="fact-num">01</div>
        <div><h3>Was wir für Sie tun können?</h3>
        <p>Wir sorgen dafür, dass Ihnen Ihre Spezialisten und Teams schnellstens zur Verfügung stehen. Und das selbst für anspruchsvolle ICT- und Business-Projekte. Vielleicht suchen Sie nur einen einzelnen Fachspezialisten oder vielleicht eine gesamte Projekt-Taskforce. Wir finden die Spezialisten, die Sie benötigen und sichern so Ihren Erfolg.</p></div>
      </div>
      <div class="fact">
        <div class="fact-num">02</div>
        <div><h3>Was uns so besonders macht?</h3>
        <p>Bei der Auswahl der Kandidaten zählt natürlich die fachliche Kompetenz, aber auch die persönliche. Im Rahmen unserer 360-Grad-Kompetenzbeurteilung sorgen wir dafür, dass der perfekte Kandidat bei unseren Kunden zum Einsatz kommt. Dank unserer über 25-jährigen Expertise und unserer Datenbank mit über 7.000 Freelancern finden wir immer den Kandidaten, der am besten zu Ihrem Projekt passt.</p></div>
      </div>
      <div class="fact">
        <div class="fact-num">03</div>
        <div><h3>Was für uns spricht?</h3>
        <p>Die meisten unserer Kunden arbeiten seit Jahrzehnten mit uns zusammen. Vielleicht ist es unsere persönliche Beratung und Betreuung. Die Schweizerische Präzision. Vielleicht schätzen uns die Kunden auch, weil wir dank der inhabergeführten Unternehmenskultur ein Stück Verlässlichkeit und Kontinuität in dieser schnelllebigen Zeit bieten können.</p></div>
      </div>
    </div>

    <div class="closing">
      Finden Sie es am besten selbst heraus. Lernen Sie uns kennen, und überzeugen Sie sich selbst, wie Sie von uns profitieren können.
      <strong>Herzlich willkommen bei Weidmann &amp; Kollegen,</strong>
      Ihr Reto Albrecht
      <span class="signature" role="img" aria-label="Handschriftliche Unterschrift des CEO"></span>
    </div>
    <div class="rule-vertical"></div>
    <div class="folio-right">03</div>
  </section>
</main>
</body>
</html>
```